Plumbing Product Supply Company Needs Front & Back Cover Design For Instruction Manuals

We need a front and back over design for our instruction manuals that we need to give to clients.

There will also be a picture of the product on the front cover so please use the supplied image as dummy.

it needs to incorporate our logo and branding colours.

We are the industry leader so it needs to be up-market, professional and stand out from the crowd.

Target Market(s)

Plumbing Companies

Industry/Entity Type

Plumbing

Font styles to use
Sans Serif

Colors
abd036
ffffff
000000
eaeaea
cbcbcb

Requirements
Must have
• Front & Back Cover as it will become a booklet.
• The logo is to be on the black background.
Nice to have
• Professional, modern, sleek.
Should not have
• Other colours that what is on the guidelines.

```html
<!DOCTYPE html>
<html lang="en">
<head>
<meta charset="utf-8">
<title>Southline Pipe Relining Supplies – Manual Covers</title>
<link rel="stylesheet" href="https://fonts.googleapis.com/css2?family=Lato:wght@400;700&family=Montserrat:wght@600&display=swap">
<style>
  :root {
    --green: #abd036;
    --green-deep: #5e9c2c;
    --black: #000000;
    --white: #ffffff;
    --light: #eaeaea;
    --mid: #cbcbcb;
    --backdrop: #e6e7e8;
  }
  * { margin: 0; padding: 0; box-sizing: border-box; }
  html, body { width: 1200px; height: 897px; overflow: hidden; background: var(--backdrop); }
  .canvas { position: relative; width: 1200px; height: 897px; }
  .cover {
    position: absolute; top: 106px; width: 484px; height: 685px;
    overflow: hidden; box-shadow: 0 2px 6px rgba(0,0,0,.25);
  }
  .cover--back { left: 102px; }
  .cover--front { left: 614px; }
  .cover__art { position: absolute; inset: 0; width: 100%; height: 100%; }
  .brand {
    position: absolute; left: 0; right: 0; text-align: center;
    font-family: "Montserrat", sans-serif; font-weight: 600; color: var(--green);
    line-height: 1;
  }
  .brand__name { display: block; }
  .brand__tag { display: block; }
  .cover--back .brand { top: 290px; }
  .cover--back .brand__name { font-size: 34px; letter-spacing: 2px; }
  .cover--back .brand__tag { font-size: 11px; letter-spacing: 2px; margin-top: 10px; }
  .cover--front .brand { top: 68px; }
  .cover--front .brand__name { font-size: 62px; letter-spacing: 3px; }
  .cover--front .brand__tag { font-size: 19px; letter-spacing: 3px; margin-top: 18px; }
  .contact {
    position: absolute; left: 0; right: 0; top: 590px; text-align: center;
    font-family: "Lato", sans-serif; color: var(--black);
  }
  .contact__title { font-size: 16px; font-weight: 700; margin-bottom: 5px; }
  .contact__line { font-size: 9.5px; font-weight: 700; line-height: 1.3; }
  .product-photo {
    position: absolute; left: 38px; top: 326px; width: 412px; height: 324px;
    border-radius: 6px;
    background: radial-gradient(ellipse at 50% 50%, #8a8a8a 0%, #c9c9c9 55%, rgba(234,234,234,0) 78%);
  }
</style>
</head>
<body>
<div class="canvas">

  <section class="cover cover--back">
    <svg class="cover__art" viewBox="0 0 606 857" preserveAspectRatio="none" aria-hidden="true">
      <defs>
        <linearGradient id="backSwoosh" x1="0" y1="0" x2="1" y2="0">
          <stop offset="0" stop-color="#5e9c2c"/>
          <stop offset=".5" stop-color="#abd036"/>
          <stop offset="1" stop-color="#5e9c2c"/>
        </linearGradient>
      </defs>
      <rect width="606" height="857" fill="#000"/>
      <path d="M0,610 Q250,540 606,630 L606,712 Q300,520 0,680 Z" fill="url(#backSwoosh)"/>
      <path d="M0,648 Q120,590 240,572 Q110,600 0,662 Z" fill="#000"/>
      <path d="M300,604 Q470,600 606,676 L606,690 Q460,612 300,604 Z" fill="#000"/>
      <path d="M0,680 Q300,520 606,712 L606,857 L0,857 Z" fill="#fff"/>
    </svg>
    <div class="brand">
      <span class="brand__name">SOUTHLINE</span>
      <span class="brand__tag">PIPE RELINING SUPPLIES</span>
    </div>
    <div class="contact">
      <p class="contact__title">Contact Us:</p>
      <p class="contact__line">Lorem ipsum Lorem ipsum Lorem ipsum Lorem ipsum</p>
      <p class="contact__line">Email: hello@southlinerelining.com | Ph: 000 000 0000 | Fax: 000 000 0000</p>
    </div>
  </section>

  <section class="cover cover--front">
    <svg class="cover__art" viewBox="0 0 606 857" preserveAspectRatio="none" aria-hidden="true">
      <defs>
        <linearGradient id="frontSwoosh" x1="0" y1="0" x2="1" y2="0">
          <stop offset="0" stop-color="#abd036"/>
          <stop offset=".5" stop-color="#5e9c2c"/>
          <stop offset="1" stop-color="#abd036"/>
        </linearGradient>
        <linearGradient id="frontPaper" x1="0" y1="0" x2="0" y2="1">
          <stop offset=".4" stop-color="#fff"/>
          <stop offset="1" stop-color="#eaeaea"/>
        </linearGradient>
      </defs>
      <rect width="606" height="857" fill="#000"/>
      <path d="M0,218 Q300,400 606,248 L606,280 Q300,440 0,300 Z" fill="url(#frontSwoosh)"/>
      <path d="M0,238 Q150,300 300,322 Q140,310 0,252 Z" fill="#000"/>
      <path d="M370,346 Q500,320 606,262 L606,270 Q500,334 370,346 Z" fill="#fff"/>
      <path d="M0,300 Q300,440 606,280 L606,857 L0,857 Z" fill="url(#frontPaper)"/>
    </svg>
    <div class="brand">
      <span class="brand__name">SOUTHLINE</span>
      <span class="brand__tag">PIPE RELINING SUPPLIES</span>
    </div>
    <div class="product-photo" role="img" aria-label="Product photo: pipe relining kit with tool case, resin containers, liner rolls, air hose, pump and inversion rods"></div>
  </section>

</div>
</body>
</html>
```